Aged Care Consultancy Business needs a business card design

I need a two sided business card - I want it clean and professional. Surprise me

Target Market(s)

middle aged and ageing victorians

Industry/Entity Type

Health Care

Contact Information for Business Card

Text to be included

Logo
Aged Care Consulting Services
Professional, Reliable, Affordable

Tovan Brelsick
Director
0427 31 64 92 (larger)
1300 73 29 41
tovan@wadolire.com.au
www.wadolcare.com.au
Facebook (details TBA)

include little icons beside the contact info:

- Envelope = email
- Phone = phone
- Globe = website

Font styles to use
Serif
Sans Serif

Requirements
Must have
• look proffesional and clean

```html
<!DOCTYPE html>
<html lang="en">
<head>
<meta charset="utf-8">
<title>wadol care – business card</title>
<link rel="stylesheet" href="https://fonts.googleapis.com/css2?family=Source+Sans+3:wght@400;600;700&display=swap">
<style>
  :root {
    --stage: #000000;
    --card-light: #f3f3f3;
    --brand-blue: #043f7c;
    --brand-navy: #0b3f7f;
    --brand-orange: #e8940c;
    --white: #ffffff;
  }
  * { margin: 0; padding: 0; box-sizing: border-box; }
  html, body {
    width: 1200px; height: 900px; overflow: hidden;
    background: var(--stage);
    font-family: "Source Sans 3", "Segoe UI", Arial, sans-serif;
  }
  .canvas { position: relative; width: 1200px; height: 900px; }

  .card { position: absolute; top: 200px; width: 310px; height: 502px; }
  .card--front {
    left: 265px; background: var(--card-light);
    border-radius: 62px 0 62px 0;
  }
  .card--back {
    left: 641px; width: 309px; background: var(--brand-blue);
    border-radius: 0 62px 0 62px;
  }

  .brand-name {
    position: absolute; left: 0; right: 0; text-align: center;
    font-weight: 700; letter-spacing: 0.5px; line-height: 1;
  }
  .card--front .brand-name { top: 139px; font-size: 46px; color: var(--brand-navy); }

  .holder { position: absolute; left: 27px; top: 305px; color: var(--brand-navy); }
  .holder__name { font-size: 19px; font-weight: 700; line-height: 1.1; }
  .holder__first { color: var(--brand-orange); }
  .holder__role { font-size: 14px; margin-top: 0; }

  .contact { position: absolute; left: 28px; list-style: none; color: var(--brand-navy); }
  .contact--main { top: 363px; }
  .contact--list { top: 394px; }
  .contact li { display: flex; align-items: center; height: 20.5px; font-size: 14.5px; }
  .contact--main li { font-size: 16.5px; font-weight: 700; }
  .contact .icon { width: 11px; height: 11px; margin-right: 7px; fill: var(--brand-orange); flex: none; }
  .contact--main .icon { width: 15px; height: 15px; margin-right: 8px; }
  .icon-square { width: 9px; height: 9px; margin: 0 8px 0 1px; background: var(--brand-orange); border-radius: 1px; flex: none; }

  .back-mark { position: absolute; left: 0; right: 0; top: 254px; text-align: center; }
  .back-mark__dot {
    display: inline-block; width: 22px; height: 22px; border-radius: 50%;
    background: var(--brand-orange); vertical-align: middle; margin-right: 10px;
  }
  .card--back .brand-name {
    position: static; display: inline; vertical-align: middle;
    font-size: 50px; color: var(--white);
  }
  .tagline {
    position: absolute; left: 0; right: 0; top: 406px; text-align: center;
    color: var(--white); font-size: 17px; font-weight: 600; line-height: 21px;
  }
</style>
</head>
<body>
<main class="canvas">
  <section class="card card--front">
    <div class="brand-name">wadol care</div>

    <div class="holder">
      <div class="holder__name"><span class="holder__first">Tovan</span> Brelsick</div>
      <div class="holder__role">Director</div>
    </div>

    <ul class="contact contact--main">
      <li>
        <svg class="icon" viewBox="0 0 24 24"><path d="M6.6 10.8a15.1 15.1 0 0 0 6.6 6.6l2.2-2.2a1 1 0 0 1 1-.25 11.4 11.4 0 0 0 3.6.57 1 1 0 0 1 1 1V20a1 1 0 0 1-1 1A17 17 0 0 1 3 4a1 1 0 0 1 1-1h3.5a1 1 0 0 1 1 1c0 1.25.2 2.45.57 3.57a1 1 0 0 1-.25 1z"/></svg>
        0427 31 64 92
      </li>
    </ul>

    <ul class="contact contact--list">
      <li>
        <svg class="icon" viewBox="0 0 24 24"><path d="M6.6 10.8a15.1 15.1 0 0 0 6.6 6.6l2.2-2.2a1 1 0 0 1 1-.25 11.4 11.4 0 0 0 3.6.57 1 1 0 0 1 1 1V20a1 1 0 0 1-1 1A17 17 0 0 1 3 4a1 1 0 0 1 1-1h3.5a1 1 0 0 1 1 1c0 1.25.2 2.45.57 3.57a1 1 0 0 1-.25 1z"/></svg>
        1300 73 29 41
      </li>
      <li>
        <svg class="icon" viewBox="0 0 24 24"><path d="M2 5h20v2.2l-10 7-10-7z"/><path d="M2 9.3l10 7 10-7V19H2z"/></svg>
        tovan@wadolire.com.au
      </li>
      <li>
        <svg class="icon" viewBox="0 0 24 24"><circle cx="12" cy="12" r="10"/><path d="M2 12h20M12 2c3 3 3 17 0 20M12 2c-3 3-3 17 0 20" fill="none" stroke="var(--card-light)" stroke-width="1.6"/></svg>
        www.wadolcare.com.au
      </li>
      <li>
        <span class="icon-square"></span>
        linkhive.net/wadolcare
      </li>
    </ul>
  </section>

  <section class="card card--back">
    <div class="back-mark">
      <span class="back-mark__dot"></span><span class="brand-name">wadol care</span>
    </div>
    <p class="tagline">Aged Care Consulting Services<br>Professional, Reliable, Affordable</p>
  </section>
</main>
</body>
</html>
```